Coffeeshop menu for filter tip

We want to have a cannabis (coffeeshop) menu in the size 25mm wide x 60mm wide. Some examples attached.

it must have the following text:
Menu

WEED p/g
Velotrine €16
Cinderfox €14
Tide Rambler €14
Marigolden €16
Grand Pelican €14
Copper Comet €14

HASH p/g
Baltic Ember €12
Harbor Velvet€11
Plum Rova €14
Dusk Maple €10

Target Market(s)

tourist in Amsterdam

Requirements
Nice to have
• cannabis sign leaf
• No Cigarettes allowed symbol

```html
<!DOCTYPE html>
<html lang="en">
<head>
<meta charset="utf-8">
<title>Coffeeshop Menu</title>
<link rel="stylesheet" href="https://fonts.googleapis.com/css2?family=Kaushan+Script&family=Roboto:wght@300;500;700&display=swap">
<style>
  :root {
    --page: #ffffff;
    --leaf-deep: #1f4512;
    --leaf-mid: #2f5f1c;
    --leaf-light: #3f7a26;
    --header-band: rgba(80, 130, 40, 0.25);
    --lime: #a4f54a;
    --no-red: #e01b1b;
  }
  * { margin: 0; padding: 0; box-sizing: border-box; }
  html, body {
    width: 800px; height: 1200px; overflow: hidden;
    background: var(--page);
  }
  .canvas { position: relative; width: 800px; height: 1200px; }

  .menu-card {
    position: absolute; left: 222px; top: 138px;
    width: 373px; height: 894px;
    overflow: hidden;
    box-shadow: 0 2px 10px rgba(0, 0, 0, 0.45);
    color: var(--lime);
    font-family: "Roboto", sans-serif;
  }
  .leaf-backdrop {
    position: absolute; inset: 0;
    background:
      radial-gradient(ellipse at 45% 55%, var(--leaf-light) 0%, transparent 60%),
      radial-gradient(ellipse at 20% 85%, var(--leaf-mid) 0%, transparent 55%),
      linear-gradient(180deg, var(--leaf-mid) 0%, var(--leaf-deep) 100%);
  }
  .title-band {
    position: absolute; left: 0; top: 0; width: 100%; height: 117px;
    background: var(--header-band);
  }
  .menu-title {
    position: absolute; left: 0; top: 22px; width: 100%;
    text-align: center;
    font-family: "Kaushan Script", cursive;
    font-size: 66px; line-height: 1;
    letter-spacing: 1px;
  }

  .section-head {
    position: absolute; left: 24px; right: 22px;
    display: flex; justify-content: space-between;
    font-size: 45px; line-height: 1;
  }
  .section-head .category { font-weight: 700; }
  .section-head .unit { font-weight: 500; }
  .weed-head { top: 170px; }
  .hash-head { top: 560px; }

  .price-list {
    position: absolute; left: 24px; right: 26px;
    list-style: none;
  }
  .weed-list { top: 226px; }
  .hash-list { top: 615px; }
  .price-list li {
    display: flex; justify-content: space-between;
    height: 44px; line-height: 44px;
    font-size: 36px; font-weight: 500;
    white-space: nowrap;
  }

  .house-rule {
    position: absolute; left: 66px; top: 840px;
    display: flex; align-items: center; gap: 16px;
    font-size: 30px; font-weight: 300; line-height: 1;
  }
  .house-rule svg { width: 38px; height: 38px; flex: none; }
</style>
</head>
<body>
<div class="canvas">
  <section class="menu-card">
    <div class="leaf-backdrop" role="img" aria-label="Soft green backdrop of cannabis leaves"></div>
    <div class="title-band"></div>
    <h1 class="menu-title">Menu</h1>

    <div class="section-head weed-head"><span class="category">WEED</span><span class="unit">p/g</span></div>
    <ul class="price-list weed-list">
      <li><span>Velotrine</span><span>€16</span></li>
      <li><span>Cinderfox</span><span>€14</span></li>
      <li><span>Tide Rambler</span><span>€14</span></li>
      <li><span>Marigolden</span><span>€16</span></li>
      <li><span>Grand Pelican</span><span>€14</span></li>
      <li><span>Copper Comet</span><span>€14</span></li>
    </ul>

    <div class="section-head hash-head"><span class="category">HASH</span><span class="unit">p/g</span></div>
    <ul class="price-list hash-list">
      <li><span>Baltic Ember</span><span>€12</span></li>
      <li><span>Harbor Velvet</span><span>€ 11</span></li>
      <li><span>Plum Rova</span><span>€14</span></li>
      <li><span>Dusk Maple</span><span>€10</span></li>
    </ul>

    <div class="house-rule">
      <svg viewBox="0 0 40 40" aria-hidden="true">
        <circle cx="20" cy="20" r="18" fill="#ffffff" stroke="var(--no-red)" stroke-width="3"/>
        <rect x="6" y="19" width="20" height="5" fill="#f2f2f2" stroke="#555" stroke-width="0.6"/>
        <rect x="6" y="19" width="6" height="5" fill="#e8a030"/>
        <rect x="26" y="19" width="4" height="5" fill="#c0392b"/>
        <path d="M31 17 q2 -4 0 -8" fill="none" stroke="#888" stroke-width="1.2"/>
        <line x1="7.5" y1="7.5" x2="32.5" y2="32.5" stroke="var(--no-red)" stroke-width="3"/>
      </svg>
      <span>No Cigarettes</span>
    </div>
  </section>
</div>
</body>
</html>
```